Harbor & Crest Real estate

Design of business plans and presentations before and after of assets is required.
The design is of PowerPoint files and needs to be tailored to the US real estate market.
Graphs and relevant information is required about the area where the company property, Cincinnati Ohio is located.
To get acquainted with the logo, colors and guidelines of the existing company design, visit the website- www.hcqholdings.com

Seeking designer for long term collaborative work.

Font styles to use
Sans Serif

```html
<!DOCTYPE html>
<html lang="en">
<head>
<meta charset="utf-8">
<title>Linwood Project – Plans vs Execution</title>
<link href="https://fonts.googleapis.com/css2?family=Montserrat:wght@400;600;700;800&family=Open+Sans:wght@400;600&display=swap" rel="stylesheet">
<style>
:root{
  --yellow:#f6c312;
  --ink:#1e1e1e;
  --grey:#6d6d6d;
  --light:#f2f2f2;
  --line:#d4d4d4;
  --canvas:#e9e9e9;
  --white:#ffffff;
}
*{box-sizing:border-box;margin:0;padding:0}
html,body{width:1200px;height:2528px;overflow:hidden;background:var(--canvas)}
body{position:relative;font-family:"Open Sans",Arial,sans-serif;color:var(--ink)}
.slide{position:absolute;width:592px;height:820px;background:var(--white);overflow:hidden}
.s1{left:0;top:0}.s2{left:608px;top:0}
.s3{left:0;top:854px}.s4{left:608px;top:854px}
.s5{left:0;top:1708px}.s6{left:608px;top:1708px}
.topbar{position:absolute;left:0;top:0;width:100%;height:14px;background:var(--ink)}
.page-no{position:absolute;right:24px;top:0;width:36px;height:22px;background:var(--yellow);font:700 11px "Montserrat",sans-serif;text-align:center;line-height:22px}
.title{position:absolute;font-family:"Montserrat",sans-serif;font-weight:800;font-size:30px;line-height:1.1}
.title-bar{position:absolute;left:0;width:180px;height:10px;background:var(--yellow)}
.brand{position:absolute;display:flex;align-items:center;gap:6px;font:700 11px "Montserrat",sans-serif;color:var(--ink)}
.brand .sq{width:14px;height:14px;background:var(--yellow)}
.ph{position:absolute}
.body-text{position:absolute;font-size:10px;line-height:1.5;color:var(--grey)}
.sub{position:absolute;font:700 13px "Montserrat",sans-serif;text-align:center}
.kpi{position:absolute;width:170px;height:54px;background:var(--yellow);font:800 26px "Montserrat",sans-serif;text-align:center;line-height:54px}
table{border-collapse:collapse;font-size:9.5px;width:100%}
th{background:var(--yellow);font:700 9.5px "Montserrat",sans-serif;text-align:left;padding:6px 8px}
td{padding:5px 8px;border-bottom:1px solid var(--line);color:var(--grey)}
tr:nth-child(even) td{background:var(--light)}
td.tick{color:var(--grey)}
td.tick:before{content:"✓ ";color:var(--ink);font-weight:700}
.tag{position:absolute;font:700 11px "Montserrat",sans-serif;color:var(--ink);background:var(--yellow);padding:4px 10px}
ul.bul{position:absolute;list-style:none;font-size:10px;line-height:1.7;color:var(--grey)}
ul.bul li:before{content:"✓ ";color:var(--ink);font-weight:700}
.q-labels{position:absolute;height:16px;font:700 12px "Montserrat",sans-serif;color:var(--ink)}
.q-labels span{position:absolute;top:0}
.footer-line{position:absolute;left:0;bottom:0;width:100%;height:6px;background:var(--ink)}
</style>
</head>
<body>

<!-- Cover -->
<section class="slide s1">
  <div class="ph" role="img" aria-label="Architectural floor plan drawing in grey line work" style="left:0;top:0;width:592px;height:600px;background:linear-gradient(135deg,#f7f7f7,#dcdcdc)"></div>
  <div class="ph" style="left:112px;top:70px;width:210px;height:170px;background:var(--yellow);padding:24px 20px">
    <div style="font:800 34px/1.05 'Montserrat',sans-serif">Linwood Project</div>
    <div style="font:600 12px 'Montserrat',sans-serif;margin-top:12px">Plans vs<br>Execution</div>
  </div>
  <div class="ph" role="img" aria-label="Renovated living room photograph" style="left:0;top:600px;width:200px;height:160px;background:linear-gradient(160deg,#8a6f55,#3d342c)"></div>
  <div class="ph" role="img" aria-label="Interior staircase photograph" style="left:200px;top:600px;width:200px;height:160px;background:linear-gradient(160deg,#b9a48a,#5a4b3d)"></div>
  <div class="brand" style="left:420px;top:676px;flex-direction:column;width:150px;text-align:center"><span class="sq"></span>Harbor &amp; Crest Real estate</div>
  <div class="ph" style="left:0;top:760px;width:592px;height:60px;background:var(--ink)"></div>
</section>

<!-- Background & location -->
<section class="slide s2">
  <div class="topbar"></div><div class="page-no">2</div>
  <div class="title" style="left:150px;top:48px">Linwood Project</div>
  <div class="title-bar" style="top:60px;width:120px"></div>
  <div class="ph" style="left:40px;top:108px;width:64px;height:190px;background:var(--yellow)"></div>
  <div class="ph" style="left:40px;top:108px;width:64px;height:190px;display:flex;align-items:center;justify-content:center"><span style="transform:rotate(-90deg);font:700 12px 'Montserrat',sans-serif;white-space:nowrap">BACKGROUND</span></div>
  <div class="body-text" style="left:124px;top:108px;width:430px">
    <p>Harbor &amp; Crest is an investment and renovation management company. Our partners use deep local knowledge and disciplined capital to reposition mid-market residential assets for long-term rental income and stable returns.</p>
    <p style="margin-top:8px">This project is a multi-family building acquired below market value. The plan targets a full renovation, new tenancy and stabilisation within one year of closing.</p>
    <p style="margin-top:8px">The following pages compare the original business plan with the actual execution, covering budget, timeline, rent levels and occupancy.</p>
  </div>
  <div class="sub" style="left:0;top:330px;width:592px">LOCATING THE TRANSACTION</div>
  <div class="ph" style="left:236px;top:352px;width:120px;height:4px;background:var(--yellow)"></div>
  <div class="body-text" style="left:40px;top:372px;width:512px">
    <p>The property sits in a walkable residential neighbourhood of Cincinnati, Ohio, close to transit, schools and retail corridors. Demand for quality rental units remains strong while supply of renovated stock is limited.</p>
    <p style="margin-top:8px">Recent employment growth and steady household formation support rent increases, and the area has seen consistent appreciation over the last decade.</p>
  </div>
  <div class="ph" role="img" aria-label="Street map of the property neighbourhood" style="left:40px;top:520px;width:340px;height:250px;background:linear-gradient(135deg,#dfe6d8,#b8c4b0)"></div>
  <div class="ph" role="img" aria-label="Aerial photograph of the property location" style="left:392px;top:520px;width:160px;height:250px;background:linear-gradient(135deg,#7d8f6a,#4e5c43)"></div>
  <div class="brand" style="left:40px;top:786px"><span class="sq"></span>Harbor &amp; Crest Real estate</div>
</section>

<!-- Plans -->
<section class="slide s3">
  <div class="topbar"></div><div class="page-no">3</div>
  <div class="title" style="left:40px;top:42px">Plans</div>
  <div class="sub" style="left:0;top:96px;width:592px;font-weight:600;font-size:12px">Asset Status at Location Time</div>
  <div class="kpi" style="left:26px;top:122px">66%</div>
  <div class="kpi" style="left:211px;top:122px;background:var(--ink);color:var(--white)">$ 3,600</div>
  <div class="kpi" style="left:396px;top:122px">$ 475,000</div>
  <div class="body-text" style="left:26px;top:180px;width:540px;display:flex;justify-content:space-between;font-size:9px"><span style="width:170px;text-align:center">Occupancy</span><span style="width:170px;text-align:center">Monthly rent</span><span style="width:170px;text-align:center">Purchase price</span></div>
  <div class="sub" style="left:26px;top:206px;text-align:left">Value Add Investment Strategy</div>
  <svg class="ph" style="left:40px;top:238px" width="90" height="80" viewBox="0 0 90 80" aria-hidden="true">
    <path d="M10 40 L45 10 L80 40" fill="none" stroke="#1e1e1e" stroke-width="4"/>
    <rect x="20" y="38" width="50" height="36" fill="none" stroke="#1e1e1e" stroke-width="4"/>
    <rect x="38" y="50" width="14" height="24" fill="#f6c312"/>
  </svg>
  <ul class="bul" style="left:150px;top:234px;width:410px">
    <li>Acquire the asset below market value with vacant units</li>
    <li>Renovate kitchens, bathrooms and common areas</li>
    <li>Re-lease units at market rent with screened tenants</li>
    <li>Stabilise occupancy and refinance to return capital</li>
  </ul>
  <div class="ph" role="img" aria-label="Scanned settlement statement document" style="left:26px;top:350px;width:540px;height:430px;background:linear-gradient(180deg,#fafafa,#e4e4e4);border:1px solid var(--line)"></div>
  <div class="footer-line"></div>
</section>

<!-- Business plan expectations -->
<section class="slide s4">
  <div class="topbar"></div><div class="page-no">4</div>
  <div class="title" style="left:40px;top:42px">Business Plan Expectations</div>
  <div class="ph" style="left:30px;top:96px;width:532px">
    <table>
      <tr><th style="width:46%">RENOVATION AND BUDGET PLAN</th><th>KEY DATA</th><th></th></tr>
      <tr><td class="tick">Replacing roof</td><td>Expected rent</td><td>$1,150</td></tr>
      <tr><td class="tick">Replacing windows</td><td>Expected occupancy</td><td>95%</td></tr>
      <tr><td class="tick">Renovation of units and bathrooms</td><td>Renovation time</td><td>4 months</td></tr>
      <tr><td class="tick">Renewal of electrical appliances</td><td>Expected value</td><td>$690,000</td></tr>
      <tr><td class="tick">HVAC replacement</td><td>Cash on cash</td><td>11%</td></tr>
      <tr><td></td><td>Hold period</td><td>5 years</td></tr>
    </table>
  </div>
  <div class="tag" style="left:40px;top:300px">BUDGET $ 120,000</div>
  <div class="sub" style="left:40px;top:344px;width:512px;font-size:11px">PROJECT TIMELINE (ACQUISITION, RETENANCY, HOUSING AND STABILIZATION)</div>
  <svg class="ph" style="left:250px;top:384px" width="90" height="60" viewBox="0 0 90 60" aria-hidden="true">
    <rect x="20" y="10" width="50" height="40" rx="4" fill="none" stroke="#1e1e1e" stroke-width="4"/><path d="M30 30 L42 40 L62 20" fill="none" stroke="#f6c312" stroke-width="5"/>
  </svg>
  <div class="body-text" style="left:230px;top:450px;width:130px;text-align:center;color:var(--ink)">Completion of renovation and betterment</div>
  <div class="q-labels" style="left:30px;top:484px;width:532px"><span style="left:80px">Q1</span><span style="left:200px">Q2</span><span style="left:320px">Q3</span><span style="left:440px">Q4</span></div>
  <svg class="ph" style="left:30px;top:504px" width="532" height="50" viewBox="0 0 532 50" aria-hidden="true">
    <line x1="0" y1="25" x2="510" y2="25" stroke="#bdbdbd" stroke-width="12"/>
    <path d="M510 10 L532 25 L510 40 Z" fill="#bdbdbd"/>
    <g fill="#f6c312"><circle cx="90" cy="25" r="9"/><circle cx="210" cy="25" r="9"/><circle cx="330" cy="25" r="9"/><circle cx="450" cy="25" r="9"/></g>
  </svg>
  <svg class="ph" style="left:76px;top:570px" width="80" height="60" viewBox="0 0 80 60" aria-hidden="true">
    <rect x="14" y="16" width="52" height="36" fill="none" stroke="#1e1e1e" stroke-width="4"/><line x1="14" y1="28" x2="66" y2="28" stroke="#1e1e1e" stroke-width="4"/>
  </svg>
  <div class="body-text" style="left:50px;top:636px;width:130px;text-align:center;color:var(--ink)">Reconstruction and completion of the acquisition</div>
  <svg class="ph" style="left:436px;top:570px" width="80" height="60" viewBox="0 0 80 60" aria-hidden="true">
    <path d="M10 30 L40 6 L70 30" fill="none" stroke="#1e1e1e" stroke-width="4"/><rect x="20" y="28" width="40" height="26" fill="#1e1e1e"/><rect x="35" y="38" width="10" height="16" fill="#f6c312"/>
  </svg>
  <div class="body-text" style="left:410px;top:636px;width:130px;text-align:center;color:var(--ink)">Housing and ongoing management</div>
  <div class="footer-line"></div>
</section>

<!-- Execution -->
<section class="slide s5">
  <div class="topbar"></div><div class="page-no">5</div>
  <div class="title" style="left:160px;top:46px">Execution</div>
  <div class="title-bar" style="top:58px;width:130px"></div>
  <div class="ph" role="img" aria-label="Before renovation: living room photograph" style="left:30px;top:100px;width:260px;height:150px;background:linear-gradient(160deg,#6e5a48,#2f2822)"></div>
  <div class="ph" role="img" aria-label="Before renovation: kitchen photograph" style="left:300px;top:100px;width:262px;height:150px;background:linear-gradient(160deg,#9a8a76,#4a4036)"></div>
  <div class="ph" role="img" aria-label="Before renovation: hallway photograph" style="left:30px;top:258px;width:170px;height:150px;background:linear-gradient(160deg,#84705c,#3c332a)"></div>
  <div class="ph" role="img" aria-label="Before renovation: bathroom photograph" style="left:208px;top:258px;width:170px;height:150px;background:linear-gradient(160deg,#b2a896,#625a4e)"></div>
  <div class="ph" role="img" aria-label="Before renovation: staircase photograph" style="left:386px;top:258px;width:176px;height:150px;background:linear-gradient(160deg,#7a6a58,#36302a)"></div>
  <div class="tag" style="left:480px;top:112px">Before</div>
  <div class="ph" role="img" aria-label="After renovation: bedroom photograph" style="left:30px;top:430px;width:170px;height:160px;background:linear-gradient(160deg,#c7b9a4,#7d6c58)"></div>
  <div class="ph" role="img" aria-label="After renovation: staircase photograph" style="left:208px;top:430px;width:170px;height:160px;background:linear-gradient(160deg,#b79f80,#5d4c3a)"></div>
  <div class="ph" role="img" aria-label="After renovation: kitchen photograph" style="left:386px;top:430px;width:176px;height:160px;background:linear-gradient(160deg,#d8d2c6,#8f877a)"></div>
  <div class="ph" role="img" aria-label="After renovation: living room photograph" style="left:30px;top:598px;width:260px;height:180px;background:linear-gradient(160deg,#b49a7c,#5a4937)"></div>
  <div class="ph" role="img" aria-label="After renovation: brick building exterior photograph" style="left:300px;top:598px;width:262px;height:180px;background:linear-gradient(180deg,#9fc1e0,#a8623f 55%,#5d7a45)"></div>
  <div class="tag" style="left:484px;top:442px">After</div>
  <div class="footer-line"></div>
</section>

<!-- Plans vs execution -->
<section class="slide s6">
  <div class="topbar"></div><div class="page-no">6</div>
  <div class="title" style="left:150px;top:42px">Plans Vs. Execution</div>
  <div class="title-bar" style="top:54px;width:120px"></div>
  <div class="sub" style="left:0;top:94px;width:592px;font-size:11px;font-weight:600">TIMELINE - PLANS VS. EXECUTION</div>
  <div class="sub" style="left:0;top:116px;width:592px">Plans</div>
  <div class="body-text" style="left:60px;top:138px;width:472px;text-align:center;color:var(--ink)">The duration for the renovation and betterment process according to the business plan was 4 months.</div>
  <div class="q-labels" style="left:30px;top:184px;width:532px"><span style="left:80px">Q1</span><span style="left:200px">Q2</span><span style="left:320px">Q3</span><span style="left:440px">Q4</span></div>
  <svg class="ph" style="left:30px;top:204px" width="532" height="50" viewBox="0 0 532 50" aria-hidden="true">
    <line x1="0" y1="25" x2="510" y2="25" stroke="#bdbdbd" stroke-width="12"/>
    <path d="M510 10 L532 25 L510 40 Z" fill="#bdbdbd"/>
    <g fill="#f6c312"><circle cx="90" cy="25" r="9"/><circle cx="210" cy="25" r="9"/><circle cx="330" cy="25" r="9"/><circle cx="450" cy="25" r="9"/></g>
  </svg>
  <svg class="ph" style="left:100px;top:258px" width="80" height="46" viewBox="0 0 80 46" aria-hidden="true">
    <path d="M6 24 L22 8 L38 24" fill="none" stroke="#f6c312" stroke-width="4"/><rect x="12" y="22" width="20" height="18" fill="#f6c312"/>
    <path d="M44 24 L60 8 L76 24" fill="none" stroke="#f6c312" stroke-width="4"/><rect x="50" y="22" width="20" height="18" fill="#f6c312"/>
  </svg>
  <div class="sub" style="left:40px;top:314px;text-align:left">Execution</div>
  <div class="body-text" style="left:40px;top:336px;width:512px;color:var(--ink)">In reality, property betterment took 4 months and full occupancy took only 1 month from the end of the renovation process.</div>
  <div class="ph" style="left:30px;top:390px;width:532px">
    <table>
      <tr><th colspan="3" style="text-align:center">SUMMARY TABLE - TIMELINE - PLANS VS. EXECUTION</th></tr>
      <tr><td></td><td style="font-weight:600;color:var(--ink)">PLANS</td><td style="font-weight:600;color:var(--ink)">EXECUTION</td></tr>
      <tr><td>Expected close date</td><td>02/2020</td><td>02/2020</td></tr>
      <tr><td>Expected renovation period</td><td>4 months</td><td>4 months</td></tr>
      <tr><td>Expected renovation budget</td><td>$120,000</td><td>$116,500</td></tr>
      <tr><td>Expected occupancy date</td><td>08/2020</td><td>07/2020</td></tr>
      <tr><td>Expected occupancy rate</td><td>95%</td><td>100%</td></tr>
      <tr><td>Expected monthly rent</td><td>$1,150</td><td>$1,210</td></tr>
      <tr><td>Expected value</td><td>$690,000</td><td>$720,000</td></tr>
      <tr><td>Hold period</td><td>5 years</td><td>5 years</td></tr>
      <tr><td>Cash on cash</td><td>11%</td><td>12.4%</td></tr>
    </table>
  </div>
  <div class="footer-line"></div>
</section>

</body>
</html>
```